Bloom Where You Stand redesign book cover

A new cover for my already published book. The old cover looks great but not for a women’s self help book. Cover is killing sales. Once I explain the book it sells quickly AND gets 5 star reviews. Outside of actually explaining the book the cover scares people away. I need a new cover. ASAP! Before The yr end please.
The tag line -
Discover 10 Practical Ways To Replace negative thoughts with knowing the voice of God. This is a self help book for women 35-45 Christian but not religious. Each chapter is a hands on spiritual experience where the reader takes small tests about themselves, discover why they have negative thoughts, what they are and how to listen to God through hands on methods of listening. NOT strange type of things. They learn what 4 voices they are listening to and how to hone in on Jesus voice. There are scriptures to pray and journaling assignments. The old cover is in the brief with the write up for the back of the book. Please use the new author picture, Publishers logo (tree), barcode, and contact info from the back of the book. And yes the author name and title of the book on the spine. Lay out on the back cover needs to be interesting. You have all the info have fun with it.

Target Market(s)

Women 35-45 yrs old Christian and new believers or seekers.

Industry/Entity Type

Non profit organization. Missionary

Requirements
Must have
• Something DIFFERENT than what is there now. Something inviting. Fresh clear title
Nice to have
• Multi colors however a white stand out cover is also good.
Should not have
• Heavy religious feeling. No church steeples, Jesus faces.

```html
<!DOCTYPE html>
<html lang="en">
<head>
<meta charset="UTF-8">
<title>Bloom Where You Stand — Book Cover</title>
<link rel="stylesheet" href="https://fonts.googleapis.com/css2?family=Fraunces:opsz,wght@144,600&family=Inter:wght@600;700&display=swap">
<style>
  :root {
    --backdrop: #2e251e;
    --cover-dark: #2a1c14;
    --hair-mid: #6b4a37;
    --hair-light: #b48f7c;
    --skin: #c99a86;
    --title-cream: #fbe7c6;
    --subtitle-white: #ffffff;
  }
  * { margin: 0; padding: 0; box-sizing: border-box; }
  html, body {
    width: 1200px;
    height: 1200px;
    overflow: hidden;
    background: var(--backdrop);
  }
  .canvas {
    position: relative;
    width: 1200px;
    height: 1200px;
    background: var(--backdrop);
  }
  .book-cover {
    position: absolute;
    left: 270px;
    top: 124px;
    width: 634px;
    height: 952px;
    overflow: hidden;
    background: var(--cover-dark);
  }
  .cover-photo {
    position: absolute;
    inset: 0;
    background:
      radial-gradient(ellipse 45% 40% at 72% 48%, var(--skin) 0%, rgba(201,154,134,0.55) 40%, rgba(201,154,134,0) 75%),
      radial-gradient(ellipse 70% 30% at 40% 4%, var(--hair-light) 0%, rgba(180,143,124,0) 80%),
      linear-gradient(100deg, var(--cover-dark) 0%, var(--hair-mid) 45%, #8a6451 65%, var(--cover-dark) 100%);
  }
  .cover-title {
    position: absolute;
    left: 30px;
    top: 20px;
    font-family: "Fraunces", Georgia, serif;
    font-weight: 600;
    font-size: 140px;
    line-height: 162px;
    color: var(--title-cream);
    letter-spacing: -2px;
  }
  .cover-title span { display: block; }
  .cover-subtitle {
    position: absolute;
    left: 32px;
    top: 690px;
    font-family: "Inter", Arial, sans-serif;
    font-weight: 600;
    font-size: 21px;
    line-height: 34px;
    color: var(--subtitle-white);
  }
  .cover-subtitle span { display: block; }
  .cover-author {
    position: absolute;
    left: 30px;
    top: 872px;
    font-family: "Inter", Arial, sans-serif;
    font-weight: 700;
    font-size: 41px;
    letter-spacing: -0.5px;
    color: var(--title-cream);
  }
</style>
</head>
<body>
  <main class="canvas">
    <section class="book-cover">
      <div class="cover-photo" role="img" aria-label="Close-up photograph of a woman with long windswept hair, eyes closed, head bowed"></div>
      <h1 class="cover-title">
        <span>Bloom</span>
        <span>Where</span>
        <span>You</span>
        <span>Stand</span>
      </h1>
      <p class="cover-subtitle">
        <span>Quiet the Noise</span>
        <span>of Anxious Thoughts</span>
        <span>and Hear</span>
        <span>God's Gentle Voice</span>
      </p>
      <p class="cover-author">Dana Whitfield</p>
    </section>
  </main>
</body>
</html>
```